Business card design needed

New company based in Brisbane, Australia. Brindle Technologies. The business is focused on the delivery of network architecture design and deployment. We will provide both services and the sale of the necessary equipment to deliver the service. Cloud computing is an important element of our focus as this is an emerging market for enterprises in Queensland. Our target marketplace is medium to large corporations with complex infrastructure requirements. IT Management and above will be the typical entry point for us into these accounts. We would like to see the use of various shade of green, design should be clutter free and impress stability, trust and growth.
Updates
Hey Everyone
Just we let you all know we have changed this project to 'committed' payment status.
Looking forward to seeing the designs! Thanks for your efforts.
Best Regards
Martin
Industry/Entity Type
Architecture
Contact Information for Business Card
Brindle Technologies, Martin Coulter, Sales Director, Level 19 Harwell Court, 58 Kelvane Street, Brisbane QLD 4000, Ph +61 7 3946 2271, M +61 4 4208 6157, E martin.coulter@brindletechnologies-example.com.au
Look and feel
Each slider illustrates characteristics of the customer's brand and the style your logo design should communicate.

```html
<!DOCTYPE html>
<html lang="en">
<head>
<meta charset="utf-8">
<title>Brindle Technologies – Business Card</title>
<link href="https://fonts.googleapis.com/css2?family=Michroma&display=swap" rel="stylesheet">
<style>
  :root {
    --backdrop: #3b2a22;
    --green-light: #43b04f;
    --green-mid: #35973f;
    --green-dark: #237537;
    --paper: #ffffff;
    --paper-shade: #eeeeee;
    --ink-green: #1e6b30;
    --font-main: "Michroma", "Arial", sans-serif;
  }
  * { box-sizing: border-box; margin: 0; padding: 0; }
  html, body {
    width: 1200px; height: 900px; overflow: hidden;
    background: var(--backdrop);
    font-family: var(--font-main);
  }
  .stage { position: relative; width: 1200px; height: 900px; }

  .card {
    position: absolute;
    width: 560px; height: 320px;
    overflow: hidden;
    box-shadow: 0 10px 28px rgba(0,0,0,0.45);
  }

  /* Front */
  .card-front { left: 70px; top: 90px; background: var(--green-dark); }
  .front-shapes { position: absolute; inset: 0; }
  .services {
    position: absolute; left: 385px; top: 34px;
    list-style: none; color: var(--paper);
    font-size: 11px; letter-spacing: 2px; line-height: 1.55;
  }
  .services li { margin-bottom: 16px; }
  .front-brand {
    position: absolute; left: 36px; bottom: 44px;
    color: var(--paper); display: flex; align-items: center; gap: 14px;
  }
  .brand-square { width: 26px; height: 26px; background: var(--paper); flex: none; }
  .brand-name { font-size: 22px; letter-spacing: 5px; line-height: 1.3; text-transform: uppercase; }
  .brand-name span { display: block; font-size: 13px; letter-spacing: 4px; }

  /* Back */
  .card-back { left: 570px; top: 490px; background: linear-gradient(180deg, var(--paper), var(--paper-shade)); }
  .back-shapes { position: absolute; inset: 0; }
  .back-brand {
    position: absolute; right: 40px; top: 52px;
    color: var(--ink-green); display: flex; align-items: center; gap: 10px;
  }
  .back-brand .brand-square { width: 20px; height: 20px; background: var(--green-mid); }
  .back-brand .brand-name { font-size: 15px; letter-spacing: 3px; }
  .back-brand .brand-name span { font-size: 9px; letter-spacing: 2.5px; }
  .person { position: absolute; left: 60px; top: 118px; color: var(--ink-green); }
  .person-name { font-size: 15px; letter-spacing: 1.5px; text-transform: uppercase; }
  .person-title { font-size: 9px; letter-spacing: 1px; text-transform: uppercase; margin: 4px 0 0 34px; }
  .contact { position: absolute; color: var(--paper); font-size: 10px; letter-spacing: 1.6px; display: flex; align-items: center; gap: 6px; white-space: nowrap; }
  .contact svg { width: 12px; height: 12px; flex: none; }
  .contact-phone { left: 342px; top: 170px; }
  .contact-mobile { left: 40px; top: 210px; }
  .contact-email { left: 40px; top: 244px; font-size: 8.6px; letter-spacing: 1.2px; }
  .contact-address { left: 40px; top: 278px; font-size: 8.6px; letter-spacing: 1.2px; }
</style>
</head>
<body>
<main class="stage">

  <section class="card card-front" aria-label="Business card front">
    <svg class="front-shapes" viewBox="0 0 560 320" width="560" height="320">
      <defs>
        <linearGradient id="front-panel-fill" x1="0" y1="0" x2="0.6" y2="1">
          <stop offset="0" stop-color="var(--green-light)"/>
          <stop offset="1" stop-color="var(--green-mid)"/>
        </linearGradient>
      </defs>
      <path d="M0 0 H310 V320 H0 Z" fill="url(#front-panel-fill)"/>
      <rect x="310" y="72" width="30" height="30" fill="var(--green-light)"/>
      <rect x="262" y="122" width="48" height="24" fill="var(--green-dark)"/>
      <rect x="284" y="166" width="26" height="24" fill="var(--green-dark)"/>
      <rect x="310" y="166" width="22" height="24" fill="var(--green-mid)"/>
      <rect x="330" y="210" width="36" height="26" fill="var(--green-mid)"/>
    </svg>
    <ul class="services">
      <li>IT Management</li>
      <li>Network<br>architecture<br>design and<br>deployment</li>
      <li>Cloud computing</li>
    </ul>
    <div class="front-brand">
      <div class="brand-square"></div>
      <div class="brand-name">Brindle<span>Technologies</span></div>
    </div>
  </section>

  <section class="card card-back" aria-label="Business card back">
    <svg class="back-shapes" viewBox="0 0 560 320" width="560" height="320">
      <path d="M0 196 H330 V158 H560 V320 H0 Z" fill="var(--green-dark)"/>
      <rect x="282" y="0" width="30" height="22" fill="var(--green-dark)"/>
      <rect x="340" y="0" width="34" height="22" fill="var(--green-dark)"/>
      <rect x="524" y="172" width="36" height="28" fill="var(--paper-shade)"/>
      <rect x="524" y="228" width="36" height="28" fill="var(--paper-shade)"/>
    </svg>

    <div class="back-brand">
      <div class="brand-square"></div>
      <div class="brand-name">Brindle<span>Technologies</span></div>
    </div>

    <div class="person">
      <p class="person-name">Martin Coulter</p>
      <p class="person-title">Sales Director</p>
    </div>

    <p class="contact contact-phone">
      <svg viewBox="0 0 12 12"><circle cx="6" cy="6" r="5.3" fill="none" stroke="#fff" stroke-width="1"/><path d="M4.2 3.2 L5 4.6 L4.5 5.2 Q5.3 6.7 6.8 7.5 L7.4 7 L8.8 7.8 L8.2 8.8 Q5 8.6 3.3 4 Z" fill="#fff"/></svg>
      +61 7 3946 2271
    </p>
    <p class="contact contact-mobile">
      <svg viewBox="0 0 12 12"><rect x="3" y="0.8" width="6" height="10.4" rx="1" fill="none" stroke="#fff" stroke-width="1"/><circle cx="6" cy="9.5" r="0.6" fill="#fff"/></svg>
      +61 4 4208 6157
    </p>
    <p class="contact contact-email">martin.coulter@brindletechnologies-example.com.au</p>
    <p class="contact contact-address">Level 19 Harwell Court, 58 Kelvane Street, Brisbane QLD 4000</p>
  </section>

</main>
</body>
</html>
```